Patent Law

Need to develop a home page for a patent lawyer.

Colors should go with logo, blues...

Company Name- Corvel Tindry, PLLC

Company Overview-

I am an Intellectual Property Lawyer and focus on patents, copyrights, trademarks, & trade secrets. I work with small businesses and start ups in the chemical and biotech industries.

Why Us-

I am small firm that can provide large-firm service at a reasonable price. I also can charge flat-fees for entreprenuers in certain practice areas.

Services-
Intellectual Property
Patents
Copyrights
Trademarks
Trade secrets
Healthcare Compliance
Elder law
Wills
Trusts

Website we like-
http://www.quarnlowtide.example/ - within industry!!
http://www.vopperhask.example/
http://dulbrickovan.example/
http://thefernwoldguides.example/

Target Market(s)

My customers will be small business, specifically small start-up companies in the chemical and biotech arena.

Industry/Entity Type

Trade

Requirements
Must have
• Colors should go with logo, blues...

```html
<!DOCTYPE html>
<html lang="en">
<head>
<meta charset="utf-8">
<title>Corvel Tindry, PLLC – Intellectual Property Law</title>
<link href="https://fonts.googleapis.com/css2?family=Open+Sans:wght@400;600;700&family=Roboto+Condensed:wght@400;700&family=Noto+Serif&display=swap" rel="stylesheet">
<style>
:root{
  --sky:#04a3e5;
  --royal:#3a51a5;
  --slate:#667a86;
  --charcoal:#44525c;
  --ink:#222;
  --nav-grey:#5d6a73;
  --page:#f4f2f3;
  --link:#39c3f5;
  --hero-deep:#2c4f6e;
  --hero-light:#7ea6c2;
}
*{margin:0;padding:0;box-sizing:border-box}
html,body{width:1200px;height:920px;overflow:hidden}
body{background:var(--page);font-family:"Open Sans",sans-serif;color:var(--ink);position:relative}
a{text-decoration:none;color:inherit}

.site-header{position:absolute;top:0;left:0;width:1200px;height:160px;background:#fff;border-top:6px solid var(--sky)}
.brand{position:absolute;left:150px;top:64px;display:flex;align-items:center;gap:12px}
.brand-mark{width:34px;height:34px;border-radius:50%;background:var(--royal)}
.brand-name{font-family:"Open Sans",sans-serif;font-weight:600;font-size:19px;color:#4a5a66;letter-spacing:.5px}

.utility-bar{position:absolute;left:644px;top:0;width:406px;height:50px;background:var(--sky);border-radius:0 0 22px 22px;display:flex;align-items:center;padding:0 10px 0 10px}
.utility-phone{display:flex;align-items:center;gap:7px;color:#0d2233;font-size:18px;padding-right:13px;border-right:1px dotted #fff;height:36px}
.search{margin-left:17px;display:flex;height:32px}
.search input{width:170px;border:0;border-radius:16px 0 0 16px;padding-left:17px;font-family:"Open Sans",sans-serif;font-size:13px;color:#888;background:#fff;outline:0}
.search button{width:44px;border:0;border-radius:0 16px 16px 0;background:var(--royal);display:flex;align-items:center;justify-content:center}

.main-nav{position:absolute;right:150px;top:120px;display:flex;font-family:"Roboto Condensed",sans-serif;font-size:17px;color:var(--nav-grey)}
.main-nav a{padding:0 0}
.main-nav .sep{margin:0 10px;color:#777}
.main-nav .current{color:#1b75bb}

.hero{position:absolute;top:160px;left:0;width:1200px;height:334px}
.hero-visual{position:absolute;inset:0;background:linear-gradient(100deg,var(--hero-light) 0%,#5f8aab 35%,#3c6383 60%,var(--hero-deep) 100%)}
.hero-copy{position:absolute;left:149px;top:78px;width:360px;color:#fff}
.hero-copy h1{font-family:"Roboto Condensed",sans-serif;font-weight:700;font-size:34px;line-height:35px;text-transform:uppercase}
.hero-copy p{margin-top:22px;font-size:13.5px;line-height:22.5px}
.hero-more{display:inline-flex;align-items:center;gap:6px;margin-top:13px;font-weight:700;font-size:13.5px;color:var(--link)}
.slider-dots{position:absolute;left:571px;top:463px;display:flex;gap:6px}
.slider-dots span{width:15px;height:15px;border-radius:50%;background:#8a9aa6}
.slider-dots .active{background:var(--link)}

.features{position:absolute;left:150px;top:541px;width:900px;height:234px;display:flex}
.feature{width:225px;padding:20px 14px 0;color:#fff;position:relative}
.feature h2{font-family:"Roboto Condensed",sans-serif;font-weight:400;font-size:23px;text-transform:uppercase;margin-bottom:6px}
.feature p{font-size:13px;line-height:22.5px}
.why{background:var(--sky)}
.what{background:var(--royal)}
.news{background:var(--slate)}
.contact{background:var(--charcoal)}
.link-list{list-style:none;font-family:"Noto Serif",serif;font-size:12.5px;color:var(--link)}
.link-list li{border-bottom:1px dotted #c9d3e6;padding:3px 0 4px 20px;line-height:20px;position:relative}
.link-list li:last-child{border-bottom:0}
.link-list li::before{content:"";position:absolute;left:7px;top:10px;width:5px;height:5px;background:#aab6d8;transform:rotate(45deg)}
.news .link-list{font-family:"Open Sans",sans-serif}
.news .link-list li{line-height:22.5px}
.btn{position:absolute;left:15px;bottom:19px;background:#000;color:#fff;font-size:13px;padding:2px 12px;border-radius:2px}
.contact-lines{font-size:13px;line-height:22.5px}
.contact-row{display:flex;align-items:center;gap:8px;margin-top:10px;font-size:13px}
.contact-row a{font-family:"Noto Serif",serif;color:#9fdcf7}

.site-footer{position:absolute;left:150px;top:823px;width:900px;border-top:1px solid #c8c8c8}
.footer-nav{display:flex;align-items:center;margin-top:26px;font-size:13px;color:#222}
.footer-nav .dot{width:6px;height:6px;border-radius:50%;background:var(--sky);margin:0 15px}
.copyright{margin-top:11px;font-size:11.5px;color:#555}
.social{position:absolute;right:0;top:26px;display:flex;gap:5px}
.social a{width:42px;height:42px;display:block}
.social .s1{background:#3b66b4}
.social .s2{background:#41aee3}
.social .s3{background:#0d6ca6}
</style>
</head>
<body>

<header class="site-header">
  <a class="brand" href="#">
    <span class="brand-mark"></span>
    <span class="brand-name">CORVEL TINDRY, PLLC</span>
  </a>

  <div class="utility-bar">
    <div class="utility-phone">
      <svg width="30" height="22" viewBox="0 0 30 22"><path d="M2 8c0-4 6-6 13-6s13 2 13 6l-1 2h-5l-1-3H9L8 10H3z" fill="#fff"/><rect x="6" y="11" width="18" height="10" rx="2" fill="#fff"/><circle cx="15" cy="16" r="3" fill="#04a3e5"/></svg>
      <span>555-014-2290</span>
    </div>
    <form class="search">
      <input type="text" placeholder="Search">
      <button type="button" aria-label="Search">
        <svg width="18" height="18" viewBox="0 0 18 18"><circle cx="7" cy="7" r="5" fill="none" stroke="#7fd4f7" stroke-width="2"/><path d="M11 11l5 5" stroke="#7fd4f7" stroke-width="3" stroke-linecap="round"/></svg>
      </button>
    </form>
  </div>

  <nav class="main-nav">
    <a class="current" href="#">HOME</a><span class="sep">/</span>
    <a href="#">ABOUT US</a><span class="sep">/</span>
    <a href="#">SERVICES</a><span class="sep">/</span>
    <a href="#">RESOURCES</a><span class="sep">/</span>
    <a href="#">FEES</a><span class="sep">/</span>
    <a href="#">BLOG</a><span class="sep">/</span>
    <a href="#">COANTACT US</a>
  </nav>
</header>

<section class="hero">
  <div class="hero-visual" role="img" aria-label="Photo of large white 3D words such as brand and trademark on a blue background"></div>
  <div class="hero-copy">
    <h1>Lorem Ipsum is simply dummy</h1>
    <p>Lorem Ipsum has been the industry's standard dummy text ever since the 1500s, when an unknown printer took a galley.</p>
    <a class="hero-more" href="#">Read More
      <svg width="19" height="19" viewBox="0 0 19 19"><circle cx="9.5" cy="9.5" r="8.3" fill="none" stroke="#39c3f5" stroke-width="1.6"/><path d="M5.5 9.5h7M9.5 6.5l3 3-3 3" fill="none" stroke="#39c3f5" stroke-width="1.6"/></svg>
    </a>
  </div>
</section>
<div class="slider-dots"><span></span><span class="active"></span><span></span></div>

<section class="features">
  <article class="feature why">
    <h2>Why Us</h2>
    <p>Lorem Ipsum is simply dummy text of the printing and typesetting industry. Lorem Ipsum has been the industry's standard dummy text ever since the 1500s.</p>
    <a class="btn" href="#">Read More</a>
  </article>
  <article class="feature what">
    <h2>What We Do</h2>
    <ul class="link-list">
      <li>Intellectual Property</li>
      <li>Patents</li>
      <li>Copyrights</li>
      <li>Trademarks</li>
      <li>Trade secrets</li>
    </ul>
    <a class="btn" href="#">Read More</a>
  </article>
  <article class="feature news">
    <h2>Latest News</h2>
    <ul class="link-list">
      <li>Lorem ipsum dolor sit amet, consectetur adipiscing elit.</li>
      <li>In posuere turpis quis molestie tempus.</li>
      <li>Integer sit amet lacus porta.</li>
    </ul>
    <a class="btn" href="#">Read More</a>
  </article>
  <article class="feature contact">
    <h2>Contact Info</h2>
    <div class="contact-lines">Marlon T. Quibey<br>48 Larkspur Lane<br>Houston, TX 77002</div>
    <div class="contact-row">
      <svg width="12" height="20" viewBox="0 0 12 20"><rect x="1" y="1" width="10" height="18" rx="2" fill="none" stroke="#fff" stroke-width="1.6"/><rect x="3" y="4" width="6" height="10" fill="#fff"/></svg>
      <span>555-014-2290</span>
    </div>
    <div class="contact-row">
      <svg width="20" height="14" viewBox="0 0 20 14"><rect x="1" y="1" width="18" height="12" fill="none" stroke="#fff" stroke-width="1.4"/><path d="M1 1l9 7 9-7M1 13l7-6M19 13l-7-6" fill="none" stroke="#fff" stroke-width="1.2"/></svg>
      <a href="#">info@corveltindry.example</a>
    </div>
    <div class="contact-row">
      <svg width="16" height="19" viewBox="0 0 16 19"><path d="M8 18S1 10 1 7a7 7 0 0 1 14 0c0 3-7 11-7 11z" fill="#fff"/><circle cx="8" cy="7" r="2.6" fill="#44525c"/></svg>
      <a href="#">Location Map</a>
    </div>
  </article>
</section>

<footer class="site-footer">
  <nav class="footer-nav">
    <a href="#">Home</a><span class="dot"></span>
    <a href="#">About Us</a><span class="dot"></span>
    <a href="#">Services</a><span class="dot"></span>
    <a href="#">Resources</a><span class="dot"></span>
    <a href="#">Fees</a><span class="dot"></span>
    <a href="#">Blog</a><span class="dot"></span>
    <a href="#">Coantact Us</a>
  </nav>
  <p class="copyright">Copyright © 2014, Corvel Tindry, PLLC. All rights reserverd</p>
  <div class="social">
    <a class="s1" href="#" aria-label="Social profile 1"></a>
    <a class="s2" href="#" aria-label="Social profile 2"></a>
    <a class="s3" href="#" aria-label="Social profile 3"></a>
  </div>
</footer>

</body>
</html>
```